brightwave - Property Management DL Card

I am after a savvy designer to cut through junk mail! so many real estate agents use flyers to promote themselves and their business and usually sales. We are a property management firm (residential) and we want to represent landlords that have existing investment properties and need a quality agent to represent them. Can you help?
DL size, will be printed and delivered to mailboxes. For a look at our website go to www.brightwavehq.com.au. Keep it simple and clutter free.
it is to be double sided - with one side to be simple and clear - just our website, logo and telephone number on the back.
attached is our logo and our telephone number is 1300 42 18 96
the above are 2 essential elements to be included + our email address: admin@brightwavehq.com.au
also attached are our transparent price list

Target Market(s)
property investors,
people that manage properties themselves
Industry/Entity Type
Property Management
Other font styles liked:
- arial
Look and feel

```html
<!DOCTYPE html>
<html lang="en">
<head>
<meta charset="utf-8">
<title>brightwave – Property Management DL Card</title>
<link rel="stylesheet" href="https://fonts.googleapis.com/css2?family=Open+Sans:wght@300;400;600&display=swap">
<style>
  :root {
    --backdrop: #d8d8d8;
    --card-black: #070707;
    --pure-black: #000000;
    --sand: #e2d8b8;
    --brick: #c5402a;
    --brick-text: #d8402c;
    --white: #ffffff;
    --muted: #9a9a9a;
    --tagline: #ecc8b6;
    --photo-light: #ece9e4;
    --photo-warm: #a78a66;
    --photo-dark: #4a4036;
  }
  * { margin: 0; padding: 0; box-sizing: border-box; }
  html, body {
    width: 1200px; height: 1200px; overflow: hidden;
    background: var(--backdrop);
    font-family: "Open Sans", Arial, sans-serif;
  }
  .canvas { position: relative; width: 1200px; height: 1200px; }

  /* Front */
  .card-front {
    position: absolute; left: 122px; top: 57px; width: 997px; height: 498px;
    background: var(--card-black);
  }
  .sand-band { position: absolute; left: 0; top: 0; width: 100%; height: 66px; background: var(--sand); }
  .interior-photo {
    position: absolute; left: 0; top: 66px; width: 716px; height: 360px;
    background:
      linear-gradient(180deg, rgba(0,0,0,0) 62%, rgba(74,64,54,0.55) 78%, rgba(167,138,102,0.5) 100%),
      radial-gradient(ellipse at 50% 40%, var(--photo-warm) 0 14%, transparent 30%),
      linear-gradient(90deg, #d6d2cc 0%, var(--photo-light) 25%, #f4f2ee 50%, var(--photo-light) 75%, #d6d2cc 100%);
  }
  .brand-panel {
    position: absolute; left: 716px; top: 66px; width: 281px; height: 360px;
    display: flex; align-items: center; justify-content: center;
  }
  .brand-lockup { text-align: center; color: var(--white); }
  .brand-name { font-weight: 300; font-size: 38px; line-height: 1; letter-spacing: 0.5px; }
  .brand-descriptor { font-weight: 300; font-size: 17px; color: var(--muted); letter-spacing: 1px; margin-top: 4px; }

  .benefit-band {
    position: absolute; left: 0; top: 426px; width: 100%; height: 72px;
    background: var(--brick); color: var(--white);
  }
  .tagline {
    position: absolute; left: 52px; top: 21px;
    font-size: 20px; font-weight: 600; color: var(--tagline);
  }
  .band-divider { position: absolute; left: 421px; top: 16px; width: 1px; height: 38px; background: var(--tagline); }
  .benefit-list { position: absolute; top: 14px; list-style: none; font-size: 16px; line-height: 21px; }
  .benefit-list li::before { content: "•"; margin-right: 7px; }
  .benefit-list.col-a { left: 446px; }
  .benefit-list.col-b { left: 711px; }

  /* Back */
  .card-back {
    position: absolute; left: 119px; top: 637px; width: 1000px; height: 500px;
    background: var(--pure-black); color: var(--white);
  }
  .card-back .brand-lockup { position: absolute; left: 54px; top: 46px; text-align: left; }
  .card-back .brand-name { font-size: 42px; }
  .card-back .brand-descriptor { font-size: 19px; margin-left: 6px; }

  .contact-block {
    position: absolute; left: 558px; top: 381px;
    border-left: 1px solid var(--muted); padding-left: 21px;
    font-size: 18px; line-height: 24px; letter-spacing: 0.5px;
  }
  .contact-phone { color: var(--brick-text); }
</style>
</head>
<body>
<main class="canvas">
  <section class="card-front">
    <div class="sand-band"></div>
    <div class="interior-photo" role="img" aria-label="Bright modern living room with two dark leather sofas, a timber feature wall and a low coffee table"></div>
    <div class="brand-panel">
      <div class="brand-lockup">
        <div class="brand-name">brightwave</div>
        <div class="brand-descriptor">property group</div>
      </div>
    </div>
    <div class="benefit-band">
      <p class="tagline">Property Management specialists</p>
      <span class="band-divider"></span>
      <ul class="benefit-list col-a">
        <li>Excellent communication</li>
        <li>Minimal vacancy</li>
      </ul>
      <ul class="benefit-list col-b">
        <li>No hidden extras</li>
        <li>The best rent return</li>
      </ul>
    </div>
  </section>

  <section class="card-back">
    <div class="brand-lockup">
      <div class="brand-name">brightwave</div>
      <div class="brand-descriptor">property group</div>
    </div>
    <address class="contact-block" style="font-style: normal;">
      <div class="contact-phone">1300 42 18 96</div>
      <div>PO Box B527, Harbourview NSW, 2199</div>
      <div>admin@brightwavehq.com.au</div>
    </address>
  </section>
</main>
</body>
</html>
```